*** Business Card Design Project

As a starting point, please take a look at our website www.plentarohire.com as a starting point.

We are looking for you to design our new business cards for plentarohire, something funky, cool and potentially unusual/different.

Good luck.

Industry/Entity Type

Business

```html
<!DOCTYPE html>
<html lang="en">
<head>
<meta charset="utf-8">
<title>Plentarohire Business Cards</title>
<link rel="stylesheet" href="https://fonts.googleapis.com/css2?family=Cabin:wght@400;600;700&display=swap">
<style>
  :root {
    --orange: #e8591c;
    --ink: #3a3a3a;
    --paper: #ffffff;
    --backdrop: #e9eef3;
    --figure: #c9c9c9;
  }
  * { box-sizing: border-box; margin: 0; padding: 0; }
  html, body { width: 1200px; height: 900px; overflow: hidden; }
  body {
    background: var(--backdrop);
    font-family: "Cabin", sans-serif;
    position: relative;
  }
  .card {
    position: absolute;
    width: 520px;
    height: 316px;
    box-shadow: 0 6px 18px rgba(0,0,0,0.18);
    overflow: hidden;
  }
  .card--front { background: var(--paper); }
  .card--a { left: 60px; top: 80px; }
  .card--b { left: 620px; top: 80px; }
  .card--back {
    left: 340px; top: 480px;
    background: var(--orange);
    display: flex; align-items: center; justify-content: center;
    padding: 24px 24px;
  }
  .brand { position: absolute; left: 40px; top: 38px; }
  .brand__name {
    font-size: 36px; font-weight: 600; color: var(--ink);
    line-height: 1;
  }
  .brand__tagline {
    font-size: 15px; color: var(--ink); letter-spacing: 1px; margin-top: 8px;
  }
  .rule {
    position: absolute; left: 0; top: 104px; width: 100%; height: 26px;
    background: linear-gradient(to bottom, rgba(0,0,0,0.06), rgba(0,0,0,0));
  }
  .rule::before {
    content: ""; position: absolute; left: 0; top: 0; width: 100%; height: 3px;
    background: linear-gradient(to right, var(--orange) 0%, var(--orange) 45%, rgba(232,89,28,0) 100%);
  }
  .person { position: absolute; left: 40px; top: 140px; }
  .person__name { font-size: 18px; font-weight: 700; color: var(--orange); }
  .person__role { font-size: 11px; color: var(--ink); margin-top: 3px; }
  .contact {
    margin-top: 16px; font-size: 11px; color: var(--ink);
    display: grid; grid-template-columns: 44px auto; row-gap: 4px;
  }
  .figure {
    position: absolute; right: 50px; top: 136px; width: 110px; height: 156px;
    border-radius: 50% 50% 45% 45%;
    background: radial-gradient(ellipse at 55% 40%, #e6e6e6, var(--figure) 75%);
  }
  .statement {
    color: var(--paper); text-align: center; font-size: 18px; line-height: 1.3;
  }
  .statement .lg { font-size: 27px; }
  .statement .md { font-size: 24px; }
</style>
</head>
<body>

  <section class="card card--front card--a">
    <div class="brand">
      <div class="brand__name">plentarohire</div>
      <div class="brand__tagline">Search &amp; Selection</div>
    </div>
    <div class="rule"></div>
    <div class="person">
      <div class="person__name">Martin Kells</div>
      <div class="person__role">Managing Director</div>
      <div class="contact">
        <span>Tel:</span><span>(+44) 020 5550 1482</span>
        <span>Mob:</span><span>(+44) 077 5550 3917</span>
        <span>Email:</span><span>martin@plentarohire.com</span>
        <span>Skype:</span><span>martinplentarohire</span>
      </div>
    </div>
    <div class="figure" role="img" aria-label="Grey 3D figure leaning on a large mobile phone"></div>
  </section>

  <section class="card card--front card--b">
    <div class="brand">
      <div class="brand__name">plentarohire</div>
      <div class="brand__tagline">Search &amp; Selection</div>
    </div>
    <div class="rule"></div>
    <div class="person">
      <div class="person__name">Simon Ashford</div>
      <div class="person__role">Account Director</div>
      <div class="contact">
        <span>Tel:</span><span>(+44) 020 5550 1476</span>
        <span>Mob:</span><span>(+44) 077 5550 8264</span>
        <span>Email:</span><span>simon@plentarohire.com</span>
        <span>Skype:</span><span>simonplentarohire</span>
      </div>
    </div>
    <div class="figure" role="img" aria-label="Grey 3D figure leaning on a large mobile phone"></div>
  </section>

  <section class="card card--back">
    <p class="statement">
      <span class="md">Plentarohire</span> Search &amp; Selection is a<br>
      <span class="lg">specialist recruitment company</span><br>
      operating within the <span class="md">mobile and</span><br>
      <span class="md">digital</span> platform sectors. We do our best to<br>
      welcome <span class="md">new candidates</span> and make<br>
      <span class="md">job-hunting</span> with us a simple and<br>
      <span class="md">enjoyable experience</span>.
    </p>
  </section>

</body>
</html>
```